依頼詳細
ロゴマークは既に決定しているので、このロゴマークを使用したデザインをお願いします。法律関係の仕事ですので、堅く、シンプルでかつ信頼感と重厚感のあるデザインを希望します。弊社のイメージカラーの落ち着いたブルーをベースにしてほしいです。表裏のデザインで、裏はごくシンプルな感じでイメージしていますが、基本的なイメージは踏襲していただいてデザインは感性におまかせしたいと思います。
納品時は、記載項目詳細記載のあるものと、役職以下を空白にしたものでお願いします。
記載項目
ロゴ:添付参照
住所1:〒890−0612 鹿児島県鹿児島市桜見台4番27号 青嵐ビル7階 TEL 099-314-5926 FAX 099-314-5927
住所2:〒108−0094 東京都港区白帆台5−17−8楓葉ビル4階
TEL 03-4281-9350 FAX 099-4281-9351
マーク:QKV5, データ守秘マーク 添付参照
役職:代表
氏名:杉森 晴也
よみがな:SUGIMORI HARUYA
携帯電話番号:090−4158−6092
メールアドレス:(空白でお願いします)
ホームページアドレス:(空白でお願いします)

希望イメージ
シンプル 複雑
単色 カラフル
暗い 明るい
日常 高級
遊び心 厳粛
未来的 伝統的
女性的 男性的
希望する色
青系
納品ファイル
• 高解像度JPG (.jpg)
• イラストレーター形式 (.ai)
• PNG形式 (.png)
補足説明

```html
<!DOCTYPE html>
<html lang="ja">
<head>
<meta charset="utf-8">
<title>Meridian Labor 名刺デザイン</title>
<link rel="stylesheet" href="https://fonts.googleapis.com/css2?family=Noto+Sans+JP:wght@400;500;700&family=Noto+Serif+JP:wght@700&display=swap">
<style>
  :root {
    --navy: #12277a;
    --navy-deep: #0a1a5c;
    --blue: #1f3f9e;
    --ink: #1a1a1a;
    --muted: #555;
    --paper: #ffffff;
    --sheet: #ffffff;
    --rule: #1a1a1a;
    --badge-blue: #2d6fc4;
    --badge-grey: #9aa3b5;
  }
  * { box-sizing: border-box; margin: 0; padding: 0; }
  html, body { width: 878px; height: 1200px; overflow: hidden; background: var(--sheet); }
  body { position: relative; font-family: "Noto Sans JP", sans-serif; color: var(--ink); }

  .side-label { position: absolute; left: 36px; font-size: 22px; font-weight: 500; }
  .side-label.front { top: 8px; }
  .side-label.back { top: 596px; }

  .card { position: absolute; left: 44px; width: 790px; height: 500px; overflow: hidden; }
  .card-front { top: 48px; background: var(--paper); border: 2px solid #c9ccd4; }
  .card-back { top: 640px; background: linear-gradient(125deg, var(--navy-deep) 0%, var(--navy) 45%, var(--blue) 62%, var(--navy) 78%, var(--navy-deep) 100%); }

  .brand { position: absolute; display: flex; align-items: center; gap: 12px; }
  .brand-mark { width: 34px; height: 34px; background: var(--navy); }
  .brand-text { display: flex; flex-direction: column; }
  .brand-kind { font-size: 11px; color: var(--navy); letter-spacing: 1px; }
  .brand-name { font-size: 44px; font-weight: 500; color: var(--navy); line-height: 1; }
  .card-front .brand { left: 36px; top: 44px; }

  .person { position: absolute; left: 400px; top: 118px; }
  .person-title { font-size: 20px; font-weight: 700; color: var(--navy); margin-right: 16px; vertical-align: middle; }
  .person-name { font-family: "Noto Serif JP", serif; font-size: 44px; font-weight: 700; color: var(--navy); letter-spacing: 4px; vertical-align: middle; }
  .person-roman { font-size: 14px; color: var(--ink); margin-left: 78px; margin-top: 2px; }

  .mobile { position: absolute; left: 22px; top: 262px; font-size: 19px; }
  .mobile-rule { position: absolute; left: 16px; right: 16px; top: 292px; height: 2px; background: var(--rule); }

  .office { position: absolute; top: 302px; width: 360px; font-size: 18px; line-height: 1.2; }
  .office.kagoshima { left: 20px; }
  .office.tokyo { left: 410px; width: 270px; }
  .office-name { font-weight: 700; font-size: 18px; border-bottom: 2px solid var(--rule); padding-bottom: 2px; margin-bottom: 4px; }
  .office .zip { font-size: 13px; color: var(--muted); }

  .badges { position: absolute; right: 24px; top: 282px; display: flex; flex-direction: column; gap: 18px; align-items: center; }

  .contact-band { position: absolute; left: 0; right: 0; bottom: 0; height: 40px; background: var(--navy); color: #fff; display: flex; justify-content: center; gap: 60px; align-items: center; font-size: 18px; }

  .card-back .brand { left: 50%; top: 50%; transform: translate(-50%, -50%); gap: 16px; }
  .card-back .brand-mark { width: 54px; height: 54px; background: #fff; }
  .card-back .brand-kind { color: #fff; font-size: 16px; }
  .card-back .brand-name { color: #fff; font-size: 68px; }
</style>
</head>
<body>
  <div class="side-label front">●表面</div>
  <section class="card card-front">
    <div class="brand">
      <span class="brand-mark"></span>
      <div class="brand-text">
        <span class="brand-kind">社会保険労務士法人</span>
        <span class="brand-name">Meridian Labor</span>
      </div>
    </div>

    <div class="person">
      <span class="person-title">代表</span><span class="person-name">杉森 晴也</span>
      <div class="person-roman">Haruya Sugimori</div>
    </div>

    <div class="mobile">Mobile　090−4158−6092</div>
    <div class="mobile-rule"></div>

    <div class="office kagoshima">
      <div class="office-name">■鹿児島事務所</div>
      <div class="zip">〒890−0612</div>
      <div>鹿児島県鹿児島市桜見台4番27号</div>
      <div>青嵐ビル7階</div>
      <div>TEL 099-314-5926</div>
      <div>FAX 099-314-5927</div>
    </div>

    <div class="office tokyo">
      <div class="office-name">■東京事務所</div>
      <div class="zip">〒108−0094</div>
      <div>東京都港区白帆台5−17−8</div>
      <div>楓葉ビル4階</div>
      <div>TEL 03-4281-9350</div>
      <div>FAX 099-4281-9351</div>
    </div>

    <div class="badges">
      <svg width="56" height="56" viewBox="0 0 56 56" role="img" aria-label="QKV5 認証マーク">
        <circle cx="28" cy="28" r="26" fill="var(--badge-blue)"/>
      </svg>
      <svg width="50" height="50" viewBox="0 0 50 50" role="img" aria-label="データ守秘マーク">
        <circle cx="25" cy="25" r="23" fill="var(--badge-grey)"/>
      </svg>
    </div>

    <div class="contact-band">
      <span>Web ‣ www.meridian-labor.sample</span>
      <span>Mail ‣ info@meridian-labor.sample</span>
    </div>
  </section>

  <div class="side-label back">●裏面</div>
  <section class="card card-back" role="img" aria-label="深い青のグラデーション背景に法人名">
    <div class="brand">
      <span class="brand-mark"></span>
      <div class="brand-text">
        <span class="brand-kind">社会保険労務士法人</span>
        <span class="brand-name">Meridian Labor</span>
      </div>
    </div>
  </section>
</body>
</html>
```